Fern & Hum Holistic Body Oil, logo and label for glas bottles

I need a logo and label design for a new product that will be sold in The Netherlands first, but internationally in the future. The product is a cosmetic Argan oil combined with essential oils. There will be 4 different oils: 1. pure Argan oil, 2. Argan oil with a essential oil blend for Vata, 3. Argan oil with an essential oil blend for Pita, 4. Argan oil with an essential oil blend for Kapha.
The argan oil is 100% biological and handmade from Morocco. The essential oil blends are created by an Ayurvedic practitioner and made in Bali. The different blends Vata, Pita and Kapha refer to the different bodytypes according to Ayurveda.

Each blend will get it's own name, but they are undecided yet, so for now we can call them Vata blend, etc. or follow the names in the document in the attachment, as long as it can be adjusted later on in the design.

We need a label for the front and the back of the bottle. The bottles will be 100 or 150 ml. The label on the front needs to have the logo and brand name on it, the title of the blend and that the oil is 100% bio.
The backside will have a description of the blend (see text in attachment 'benefits' and 'blend' and instructions on how to use it (please create temporary fake text of approx. 3 lines), the website (www.fernandhum.example) and the eco certificate.

The design needs to be natural and clean. Some reference to Morocco and/or Asia is optional. It is a healthcare product. In the attachment I have added some examples of clean designs, they are just meant as inspiration, not as a fixed indication of how the design needs to be.
I WOULD LOVE TO SEE SOME DESIGNS FOR A TRANSPARANT LABEL. THE BOTTLE WILL BE TRANSPARANT GLASS< THE OIL IS A GOLDEN YELLOW COLOR.

Target Market(s)

men and women, but mostly women, age 25-50 years old, interested in healthy living, yoga, biological product, natural products, living a trendy lifestyle, having a good budget for wellness products.

Industry/Entity Type

Health And Wellness

Logo Text

Fern & Hum

Font styles to use
Serif
Decorative
Script

Requirements
Must have
• A design that is easy to adjust if there is a change in the product name. I need to be able to change the text without the available space. A connection to a healthy lifestyle, yoga, wellness, natural lifestyle. And a modern, trendy look.
Nice to have
• unique or playful ways to share the information on the bottle with graphics.
Should not have
• too much decoration and patterns, too many colors combined.

```html
<!DOCTYPE html>
<html lang="en">
<head>
<meta charset="utf-8">
<title>Fern &amp; Hum – Pitta blend label</title>
<link href="https://fonts.googleapis.com/css2?family=Overlock:wght@400;700&display=swap" rel="stylesheet">
<style>
  :root {
    --paper: #ffffff;
    --brown: #7a5638;
    --rust: #c4532b;
    --copper: #b06a3c;
    --blush: #f1e3d6;
    --olive: #8fa33e;
  }
  * { margin: 0; padding: 0; box-sizing: border-box; }
  html, body {
    width: 675px;
    height: 1200px;
    overflow: hidden;
    background: var(--paper);
  }
  .label {
    position: relative;
    width: 675px;
    height: 1200px;
    background: var(--paper);
    font-family: "Overlock", sans-serif;
    text-align: center;
  }
  .product-type {
    position: absolute;
    top: 106px;
    left: 0;
    right: 0;
    font-size: 58px;
    font-weight: 700;
    letter-spacing: 1px;
    color: var(--blush);
    -webkit-text-stroke: 2px var(--copper);
  }
  .brand-name {
    position: absolute;
    top: 206px;
    left: 0;
    right: 0;
    font-size: 34px;
    font-weight: 700;
    word-spacing: 6px;
    color: var(--brown);
  }
  .brand-mark {
    position: absolute;
    top: 258px;
    left: 50%;
    width: 110px;
    height: 110px;
    margin-left: -55px;
  }
  .blend-intro {
    position: absolute;
    top: 588px;
    left: 0;
    right: 0;
    font-size: 56px;
    font-weight: 700;
    color: var(--brown);
  }
  .blend-name {
    position: absolute;
    top: 656px;
    left: 0;
    right: 0;
    font-size: 92px;
    font-weight: 700;
    color: var(--rust);
  }
  .claims {
    position: absolute;
    top: 836px;
    left: 0;
    right: 0;
    list-style: none;
    font-size: 36px;
    font-weight: 700;
    line-height: 48px;
    color: var(--copper);
  }
</style>
</head>
<body>
  <main class="label">
    <h2 class="product-type">HOLISTIC BODY OIL</h2>
    <p class="brand-name">Fern &amp; Hum</p>
    <svg class="brand-mark" viewBox="0 0 110 110" aria-hidden="true">
      <circle cx="55" cy="55" r="55" fill="var(--olive)"/>
    </svg>
    <p class="blend-intro">I am</p>
    <h1 class="blend-name">Pitta blend</h1>
    <ul class="claims">
      <li>...with 100% bio roots...</li>
      <li>...with an Ayurvedic soul...</li>
      <li>...with a peaceful Moroccan origin...</li>
    </ul>
  </main>
</body>
</html>
```